Corvanta512 Business Card Redesign

I want to create a design for brand new business cards, I need something exceptional for clear plastic business card design. Please do not submit without it being on a clear design. Photos of the various logo versions attached.

```html
<!DOCTYPE html>
<html lang="en">
<head>
<meta charset="utf-8">
<title>Corvanta512 Business Card</title>
<link href="https://fonts.googleapis.com/css2?family=Arimo:wght@400;700&display=swap" rel="stylesheet">
<style>
  :root {
    --page-bg: #c9bfb3;
    --plastic: rgba(255, 255, 255, 0.22);
    --plastic-edge: rgba(255, 255, 255, 0.9);
    --sheen: rgba(255, 255, 255, 0.35);
    --ink: #15171e;
    --ink-soft: #22232a;
    --title: #4f4030;
    --gold: #8f6a2e;
    --gold-dark: #6e4c1c;
    --navy: #222839;
    --divider: #3f3a35;
  }
  * { margin: 0; padding: 0; box-sizing: border-box; }
  html, body {
    width: 1170px;
    height: 1200px;
    overflow: hidden;
    background: var(--page-bg);
    font-family: "Arimo", Arial, sans-serif;
  }
  .card {
    position: absolute;
    left: 85px;
    top: 314px;
    width: 1000px;
    height: 572px;
    border-radius: 28px;
    border: 2px solid var(--plastic-edge);
    background:
      linear-gradient(135deg, var(--sheen) 0%, rgba(255,255,255,0.08) 40%, rgba(255,255,255,0) 60%, rgba(255,255,255,0.12) 100%),
      var(--plastic);
    box-shadow:
      inset 0 0 0 1px rgba(255,255,255,0.35),
      inset 0 -18px 30px rgba(0,0,0,0.06),
      0 6px 18px rgba(0,0,0,0.10);
    backdrop-filter: blur(6px);
    overflow: hidden;
  }
  .brand {
    position: absolute;
    left: 0;
    width: 644px;
    top: 350px;
    text-align: center;
    font-weight: 700;
    font-size: 46px;
    letter-spacing: 1px;
    color: var(--gold);
  }
  .divider {
    position: absolute;
    left: 519px;
    top: 133px;
    width: 2px;
    height: 310px;
    background: var(--divider);
    opacity: 0.75;
  }
  .details {
    position: absolute;
    left: 553px;
    top: 136px;
    color: var(--ink-soft);
  }
  .person-name {
    font-size: 35px;
    font-weight: 700;
    color: var(--ink);
    line-height: 40px;
  }
  .person-title {
    font-size: 24px;
    color: var(--title);
    line-height: 30px;
  }
  .address {
    margin-top: 18px;
    font-size: 24px;
    line-height: 32px;
  }
  .contacts {
    list-style: none;
    margin-top: 16px;
    font-size: 24px;
    line-height: 32px;
  }
  .contacts li { display: flex; align-items: center; }
  .contacts svg { width: 20px; height: 20px; margin-right: 14px; fill: var(--ink); }
  .base-band {
    position: absolute;
    left: 0;
    bottom: 0;
    width: 100%;
    height: 12px;
    display: flex;
  }
  .band-navy { flex: 0 0 65%; background: var(--navy); }
  .band-gold { flex: 1; background: linear-gradient(90deg, var(--gold-dark), var(--gold)); }
</style>
</head>
<body>
  <div class="card">
    <div class="brand">Corvanta512</div>
    <div class="divider"></div>
    <div class="details">
      <div class="person-name">MARCUS HALE</div>
      <div class="person-title">President</div>
      <div class="address">4170 Linden Crest Road<br>Ashbury, NY 10482</div>
      <ul class="contacts">
        <li>
          <svg viewBox="0 0 20 20" aria-hidden="true"><path d="M4 1l4 4-2 3c1 2 3 4 6 6l3-2 4 4-3 3C9 18 2 11 1 4z"/></svg>
          555-201-4378
        </li>
        <li>
          <svg viewBox="0 0 20 20" aria-hidden="true"><path d="M5 0h10v20H5z M7 2v13h6V2z M9 16.5h2v2H9z" fill-rule="evenodd"/></svg>
          555-309-6214
        </li>
        <li>
          <svg viewBox="0 0 20 20" aria-hidden="true"><path d="M1 4h18v12H1z M3 6v1l7 5 7-5V6l-7 5z" fill-rule="evenodd"/></svg>
          info@corvanta512.com
        </li>
        <li>
          <svg viewBox="0 0 20 20" aria-hidden="true"><circle cx="10" cy="10" r="9"/><path d="M10 1v18M1 10h18" stroke="#d8d0c6" stroke-width="1.4"/></svg>
          www.corvanta512.com
        </li>
      </ul>
    </div>
    <div class="base-band">
      <div class="band-navy"></div>
      <div class="band-gold"></div>
    </div>
  </div>
</body>
</html>
```